Website To Serve As A Resource For plain partner badge Conditions

I need a website that is attractive that will be utilized to educate patients on either hepatitis c or HIV so it should be easily readable attractive but also professional. This website is going to be furnished with various topics for example, HIV treatment, HIV and Nutrition, HIV and Exercise, HIV and....

This website will also be cloned and utilized similarly for Hepatitis.

Coded - Design and coding required

1 page

0094D4
00A9DD
6FCCEA
C7EBF8
E9F6FB
A7469A
B969AE
D3A5CF
EDDBEB
F8F0F9
6B429C
8869AF
B7A5CE
E3DAEB
F3F0F8

```html
<!DOCTYPE html>
<html lang="en">
<head>
<meta charset="utf-8">
<title>Lorem Ipsum – Your Partner in Health and Hope</title>
<link href="https://fonts.googleapis.com/css2?family=Montserrat:wght@500;600;700;800&family=Poppins:wght@400;500;600&display=swap" rel="stylesheet">
<style>
:root{
  --blue-dark:#0094D4;
  --blue:#00A9DD;
  --blue-light:#6FCCEA;
  --blue-pale:#C7EBF8;
  --blue-mist:#E9F6FB;
  --magenta:#A7469A;
  --magenta-mid:#B969AE;
  --magenta-light:#D3A5CF;
  --magenta-pale:#EDDBEB;
  --purple:#6B429C;
  --purple-mid:#8869AF;
  --purple-light:#B7A5CE;
  --purple-pale:#E3DAEB;
  --ink:#1f1f24;
  --text:#55555f;
  --rule:#d6d6dc;
}
*{margin:0;padding:0;box-sizing:border-box}
html,body{width:1200px;height:4762px;overflow:hidden;background:#fff}
body{position:relative;font-family:"Poppins",sans-serif;color:var(--text)}
.abs{position:absolute}
h1,h2,h3,.heading{font-family:"Montserrat",sans-serif;color:var(--ink);font-weight:800}
h2{font-size:40px;letter-spacing:.3px;line-height:1}
.body-copy{font-size:13.5px;line-height:27px;color:var(--text)}
.btn{display:flex;align-items:center;justify-content:center;color:#fff;font-family:"Montserrat",sans-serif;font-weight:700;font-size:11px;letter-spacing:.6px;width:165px;height:37px}
.rule{left:135px;width:930px;height:2px;background:var(--rule)}

/* top bar */
.topbar{left:0;top:0;width:1200px;height:44px;background:linear-gradient(90deg,var(--blue-dark),var(--blue))}
.topbar .hours{left:134px;top:0;height:44px;display:flex;align-items:center;gap:12px;color:#fff;font-size:10.5px}
.topbar .social{right:134px;top:0;height:44px;display:flex;align-items:center;gap:10px;color:#fff;font-size:10.5px;font-weight:600}
.topbar .social i{display:block;width:20px;height:20px;border-radius:50%;background:#fff}

/* nav */
.nav{left:0;top:44px;width:1200px;height:76px;background:#fff}
.brand{display:flex;align-items:center;gap:10px;font-family:"Montserrat",sans-serif;font-weight:800;color:var(--ink)}
.brand .mark{border-radius:50%;background:var(--purple)}
.nav .brand{position:absolute;left:134px;top:24px;font-size:14px}
.nav .brand .mark{width:30px;height:30px}
.nav ul{position:absolute;left:433px;top:0;height:76px;display:flex;align-items:center;list-style:none;font-size:13px;color:var(--ink)}
.nav li{position:absolute;white-space:nowrap}
.nav li.active{font-weight:600}

/* hero */
.hero-photo{left:0;top:120px;width:1200px;height:675px;border-bottom-right-radius:80px;
  background:linear-gradient(100deg,#e8eef2 0%,#dfe7ec 35%,#cdd8de 55%,#d9c3a8 75%,#c9d4db 100%)}
.hero-figure{left:640px;top:180px;width:330px;height:615px;border-radius:140px 140px 0 0;background:linear-gradient(180deg,#cfd6dc,#eef1f3 40%,#dde3e8)}
.hero h1{position:absolute;left:137px;top:328px;font-size:48px;line-height:46px;width:520px}
.hero p{position:absolute;left:137px;top:482px;width:400px;font-size:13px;line-height:24px;color:#3d3d46}
.hero .btn{position:absolute;left:137px;top:583px;background:var(--blue-dark)}

/* about */
.about h2{position:absolute;left:135px;top:934px}
.about .body-copy{position:absolute;left:135px;top:986px;width:435px}
.about .btn{position:absolute;left:135px;top:1259px;background:linear-gradient(90deg,var(--purple),var(--purple-mid))}
.mission{left:630px;top:900px;width:430px;height:420px}
.mission-text{left:730px;top:1035px;width:215px;text-align:center}
.mission-text h3{font-family:"Poppins",sans-serif;font-weight:600;font-size:16px;margin-bottom:12px}
.mission-text p{font-size:11.5px;line-height:24px;color:var(--text)}

/* offer */
.offer h2{position:absolute;left:135px;top:1615px}
.offer .body-copy{position:absolute;left:135px;top:1668px;width:410px}
.offer .btn{position:absolute;left:135px;top:1941px;background:linear-gradient(90deg,var(--magenta),var(--magenta-mid))}
.service{width:200px}
.service .icon{width:96px;height:96px;border-radius:50%;background:var(--magenta);box-shadow:0 8px 16px rgba(167,70,154,.3);display:flex;align-items:center;justify-content:center}
.service h3{font-size:16px;margin:30px 0 12px;letter-spacing:.2px}
.service p{font-size:10.5px;line-height:21px;color:var(--text)}

/* why */
.why h2{position:absolute;left:135px;top:2341px}
.why .body-copy{position:absolute;left:135px;top:2394px;width:425px}
.features{left:135px;top:2596px;width:470px;height:174px;background:#fff;border-top:3px solid var(--blue-dark);box-shadow:0 4px 20px rgba(0,0,0,.08)}
.features .cell{position:absolute;display:flex;align-items:center;gap:14px;font-size:10px;line-height:13px;color:#333}
.features .vline{position:absolute;left:233px;top:18px;width:1px;height:138px;background:#e5e5ea}
.features .hline{position:absolute;left:22px;top:86px;width:426px;height:1px;background:#e5e5ea}
.doctor-photo{left:655px;top:2228px;width:345px;height:565px;background:linear-gradient(180deg,#f4f4f6,#e4e7ec 40%,#d8dce3);border-radius:150px 150px 0 0}
.doctor-name{left:700px;top:2814px;width:300px;text-align:center;font-family:"Montserrat",sans-serif;font-weight:600;font-size:20px;color:var(--ink)}

/* arrows */
.arrow{width:38px;height:38px;border-radius:50%;display:flex;align-items:center;justify-content:center}
.arrow.prev{border:2px solid var(--magenta)}
.arrow.next{background:var(--purple)}

/* testimonials */
.testi h2{position:absolute;left:135px;top:3046px}
.avatar{width:48px;height:48px;border-radius:50%}
.quote-card{width:384px;height:203px;background:#fff;box-shadow:0 4px 22px rgba(0,0,0,.08);padding:26px 30px}
.quote-card p{font-size:11.5px;line-height:22px;margin-top:20px;color:var(--text)}
.quote-card .who{text-align:right;margin-top:14px;padding-right:30px}
.quote-card .who b{display:block;font-family:"Montserrat",sans-serif;font-weight:800;font-size:13px;color:var(--ink)}
.quote-card .who span{font-size:11px}

/* news */
.news h2{position:absolute;left:135px;top:3532px}
.post{width:294px;height:398px;padding:13px 11px}
.post.featured{box-shadow:0 3px 18px rgba(0,0,0,.1);border:1px solid #eee}
.post .thumb{width:272px;height:181px}
.post h3{font-size:12px;margin:26px 12px 4px;font-weight:700}
.post .date{font-size:9.5px;color:var(--blue-dark);font-weight:600;margin-left:12px;font-family:"Montserrat",sans-serif}
.post p{font-size:10.5px;line-height:21px;margin:18px 12px 0;color:var(--text)}
.post .more{display:flex;align-items:center;gap:14px;margin:20px 12px 0;font-family:"Montserrat",sans-serif;font-weight:700;font-size:10.5px;letter-spacing:1.5px;color:var(--blue-dark)}

/* partners */
.partner{top:4110px;width:214px;height:111px;background:#f1f1f3;display:flex;align-items:center;justify-content:center}
.partner.lifted{background:#fff;box-shadow:0 4px 18px rgba(0,0,0,.12)}
.partner i{display:block;width:90px;height:34px;border-radius:6px;background:#c9c9cf}
.partner.lifted i{background:var(--blue-pale)}

/* footer */
.footer .brand{position:absolute;left:135px;top:4432px;font-size:22px;font-weight:700;color:#3a3a44}
.footer .brand .mark{width:54px;height:54px}
.footer .about-text{position:absolute;left:135px;top:4508px;width:275px;font-size:10.5px;line-height:21px}
.footer ul{position:absolute;list-style:none;font-size:10px;line-height:22px;color:var(--text)}
.copyright-rule{left:152px;top:4702px;width:898px;height:1px;background:#cfcfd5}
.copyright{left:0;top:4720px;width:1200px;text-align:center;font-size:10px;color:#555}
</style>
</head>
<body>

<!-- top bar -->
<div class="abs topbar">
  <div class="abs hours">
    <svg width="18" height="18" viewBox="0 0 18 18"><circle cx="9" cy="9" r="8" fill="none" stroke="#fff" stroke-width="1.4"/><path d="M9 4.5V9l3 2" stroke="#fff" stroke-width="1.4" fill="none" stroke-linecap="round"/></svg>
    <span>Opening Hours: Mon - Sat 8.00 - 18.00</span>
  </div>
  <div class="abs social"><span>Follow Us On:</span><i></i><i></i><i></i><i></i></div>
</div>

<!-- navigation -->
<header class="abs nav">
  <div class="brand"><span class="mark"></span>LOREM IPSUM</div>
  <ul>
    <li class="active" style="left:0">Home</li>
    <li style="left:94px">About Us</li>
    <li style="left:212px">Services</li>
    <li style="left:323px">Testimonials</li>
    <li style="left:462px">Blogs</li>
    <li style="left:554px">Contact Us</li>
  </ul>
</header>

<!-- hero -->
<section class="hero">
  <div class="abs hero-photo" role="img" aria-label="Bright hospital corridor, softly blurred"></div>
  <div class="abs hero-figure" role="img" aria-label="Smiling doctor in a white coat with a stethoscope, pointing upward"></div>
  <h1>YOUR PARTNER IN HEALTH AND HOPE</h1>
  <p>Lorem Ipsum is simply dummy text of the printing and typesetting industry. Lorem Ipsum has been the industry's standard dummy text ever since the 1500s</p>
  <div class="btn">LEARN MORE</div>
</section>

<!-- about -->
<section class="about">
  <h2>ABOUT US</h2>
  <div class="body-copy">
    <p>Lorem Ipsum is simply dummy text of the printing and typesetting industry. Lorem Ipsum has been the industry's standard dummy text ever since the 1500s.Lorem Ipsum is simply dummy text of the printing and typesetting industry. Lorem Ipsum has been the industry's standard dummy text ever since the 1500s.</p>
    <p style="margin-top:27px">Lorem Ipsum is simply dummy text of the printing and typesetting industry.</p>
  </div>
  <div class="btn">READ MORE</div>

  <svg class="abs mission" viewBox="0 0 430 420">
    <defs><marker id="tip" markerWidth="6" markerHeight="6" refX="3" refY="3" orient="auto"><path d="M0 0L6 3L0 6z" fill="#333"/></marker></defs>
    <circle cx="208" cy="210" r="198" fill="none" stroke="var(--purple)" stroke-width="1.2"/>
    <circle cx="208" cy="210" r="184" fill="none" stroke="#333" stroke-width="1.2" stroke-dasharray="560 0" opacity="0"/>
    <path d="M128 52 A184 184 0 0 0 128 368" fill="none" stroke="#333" stroke-width="1.4"/>
    <path d="M275 35 A205 205 0 0 1 393 148" fill="none" stroke="#333" stroke-width="1.4" marker-end="url(#tip)"/>
    <path d="M393 290 A205 205 0 0 1 300 385" fill="none" stroke="#333" stroke-width="1.4" marker-end="url(#tip)"/>
    <path d="M128 368 A184 184 0 0 0 180 392" fill="none" stroke="#333" stroke-width="1.4" marker-end="url(#tip)"/>
    <circle cx="208" cy="20" r="27" fill="var(--purple)"/>
    <circle cx="208" cy="20" r="10" fill="none" stroke="#fff" stroke-width="2"/><circle cx="208" cy="20" r="4" fill="#fff"/><path d="M212 16l8-8" stroke="#fff" stroke-width="2"/>
    <circle cx="402" cy="210" r="27" fill="#fff" stroke="var(--purple)" stroke-width="1.5"/>
    <path d="M390 210q12-10 24 0q-12 10-24 0z" fill="var(--purple)"/><circle cx="402" cy="210" r="3.5" fill="#fff"/>
    <circle cx="208" cy="405" r="27" fill="#fff" stroke="var(--purple)" stroke-width="1.5"/>
    <circle cx="208" cy="405" r="11" fill="var(--purple)"/><path d="M208 398v7l5 3" stroke="#fff" stroke-width="2" fill="none"/>
  </svg>
  <div class="abs mission-text">
    <h3>Our Mission</h3>
    <p>Lorem Ipsum is simply dummy text of the printing and typesetting industry. Lorem Ipsum has been the industry's standard dummy</p>
  </div>
</section>

<div class="abs rule" style="top:1429px"></div>

<!-- what we offer -->
<section class="offer">
  <h2>WHAT WE OFFER</h2>
  <div class="body-copy">
    <p>Lorem Ipsum is simply dummy text of the printing and typesetting industry. Lorem Ipsum has been the industry's standard dummy text ever since the 1500s.Lorem Ipsum is simply dummy text of the printing and typesetting industry. Lorem Ipsum has been the industry's standard dummy text ever since the 1500s.</p>
    <p style="margin-top:27px">Lorem Ipsum is simply dummy text of the printing and typesetting industry.</p>
  </div>
  <div class="btn">READ MORE</div>

  <div class="abs service" style="left:632px;top:1528px">
    <div class="icon"><svg width="44" height="44" viewBox="0 0 44 44" fill="none" stroke="#fff" stroke-width="2.2"><rect x="8" y="12" width="20" height="26" rx="3"/><path d="M12 6h12v6H12z"/><path d="M18 20v10M13 25h10"/><circle cx="34" cy="32" r="6"/></svg></div>
    <h3>HEPATITIS C</h3>
    <p>Lorem Ipsum is simply dummy text of the printing and typesetting industry. Lorem Ipsum has been the industry's standard dummy text ever since the 1500s.</p>
  </div>
  <div class="abs service" style="left:875px;top:1528px">
    <div class="icon"><svg width="44" height="44" viewBox="0 0 44 44"><circle cx="22" cy="22" r="15" fill="none" stroke="#fff" stroke-width="2.2"/><text x="22" y="27" text-anchor="middle" fill="#fff" font-family="Montserrat,sans-serif" font-size="13" font-weight="700">B+</text></svg></div>
    <h3>HEPATITIS B</h3>
    <p>Lorem Ipsum is simply dummy text of the printing and typesetting industry. Lorem Ipsum has been the industry's standard dummy text ever since the 1500s.</p>
  </div>
  <div class="abs service" style="left:632px;top:1813px">
    <div class="icon"><svg width="46" height="46" viewBox="0 0 46 46" fill="none" stroke="#fff" stroke-width="2.2"><path d="M6 22c0-10 10-12 22-10 8 2 12 6 10 12-4 8-14 6-18 12-4-4-14-4-14-14z"/><circle cx="30" cy="28" r="6"/><path d="M34 32l6 6"/></svg></div>
    <h3>HEPATITIS A</h3>
    <p>Lorem Ipsum is simply dummy text of the printing and typesetting industry. Lorem Ipsum has been the industry's standard dummy text ever since the 1500s.</p>
  </div>
  <div class="abs service" style="left:875px;top:1813px">
    <div class="icon"><svg width="48" height="48" viewBox="0 0 48 48"><circle cx="24" cy="24" r="13" fill="none" stroke="#fff" stroke-width="2.2" stroke-dasharray="3 2.5"/><circle cx="24" cy="24" r="18" fill="none" stroke="#fff" stroke-width="1.6" stroke-dasharray="2 4"/><text x="24" y="29" text-anchor="middle" fill="#fff" font-family="Montserrat,sans-serif" font-size="14" font-weight="800">E</text></svg></div>
    <h3>HEPATITIS E</h3>
    <p>Lorem Ipsum is simply dummy text of the printing and typesetting industry. Lorem Ipsum has been the industry's standard dummy text ever since the 1500s.</p>
  </div>
</section>

<div class="abs rule" style="top:2163px"></div>

<!-- why choose us -->
<section class="why">
  <h2>WHY CHOOSE US?</h2>
  <p class="body-copy">Lorem Ipsum is simply dummy text of the printing and typesetting industry. Lorem Ipsum has been the industry's standard dummy text ever since the 1500s.Lorem Ipsum is simply dummy text of the printing and typesetting industry. Lorem Ipsum has been the industry's standard dummy text ever since the 1500s.</p>
  <div class="abs features">
    <div class="vline"></div><div class="hline"></div>
    <div class="cell" style="left:32px;top:34px">
      <svg width="30" height="26" viewBox="0 0 30 26"><rect x="1" y="6" width="28" height="19" rx="3" fill="var(--blue-dark)"/><rect x="10" y="1" width="10" height="6" rx="1.5" fill="none" stroke="var(--blue-dark)" stroke-width="2"/><rect x="1" y="12" width="28" height="2" fill="#fff"/></svg>
      <span>Over 20 years of<br>experience.</span></div>
    <div class="cell" style="left:254px;top:32px">
      <svg width="30" height="30" viewBox="0 0 30 30"><circle cx="15" cy="8" r="6" fill="var(--blue-dark)"/><path d="M3 29c0-9 5-13 12-13s12 4 12 13z" fill="var(--blue-dark)"/><circle cx="20" cy="23" r="2.5" fill="#fff"/></svg>
      <span>We have experienced<br>Doctor's.</span></div>
    <div class="cell" style="left:32px;top:106px">
      <svg width="30" height="28" viewBox="0 0 30 28"><rect x="1" y="6" width="28" height="21" rx="4" fill="var(--blue-dark)"/><path d="M11 2h8v4h-8z" fill="var(--blue-dark)"/><path d="M15 11v11M9.5 16.5h11" stroke="#fff" stroke-width="3"/></svg>
      <span>Emergency Patient<br>Entries in Our Hospital.</span></div>
    <div class="cell" style="left:254px;top:104px">
      <svg width="32" height="32" viewBox="0 0 32 32"><circle cx="16" cy="16" r="13" fill="none" stroke="var(--blue-dark)" stroke-width="2.4" stroke-dasharray="62 20"/><text x="16" y="20.5" text-anchor="middle" fill="var(--blue-dark)" font-family="Montserrat,sans-serif" font-size="11" font-weight="800">24</text></svg>
      <span>24/7 Available Doctors<br>We Provide.</span></div>
  </div>
  <div class="abs doctor-photo" role="img" aria-label="Bearded doctor in a white coat with a stethoscope, gesturing with an open hand"></div>
  <div class="abs doctor-name">DR. OWEN HALE</div>
</section>

<div class="abs rule" style="top:2946px"></div>

<!-- testimonials -->
<section class="testi">
  <h2>WHAT PATIENT SAYS</h2>
  <div class="abs arrow prev" style="left:974px;top:3045px"><svg width="12" height="12" viewBox="0 0 12 12"><path d="M8 1L3 6l5 5" stroke="var(--purple)" stroke-width="2.4" fill="none"/></svg></div>
  <div class="abs arrow next" style="left:1026px;top:3045px"><svg width="12" height="12" viewBox="0 0 12 12"><path d="M4 1l5 5-5 5" stroke="#fff" stroke-width="2.4" fill="none"/></svg></div>

  <div class="abs avatar" style="left:135px;top:3136px;background:linear-gradient(180deg,#c98a5e,#e08a2a)" role="img" aria-label="Patient portrait"></div>
  <div class="abs quote-card" style="left:200px;top:3134px">
    <svg width="36" height="22" viewBox="0 0 36 22" fill="var(--purple)"><path d="M0 22V12C0 5 4 1 10 0v5c-3 1-4 3-4 6h5v11zM19 22V12c0-7 4-11 10-12v5c-3 1-4 3-4 6h5v11z"/></svg>
    <p>Lorem Ipsum is simply dummy text of the printing and typesetting industry. Lorem Ipsum has been the industry's standard dummy text ever</p>
    <div class="who"><b>MARA LIND</b><span>Manager</span></div>
  </div>

  <div class="abs avatar" style="left:618px;top:3136px;background:linear-gradient(180deg,#9aa0a8,#3b3f47)" role="img" aria-label="Patient portrait"></div>
  <div class="abs quote-card" style="left:684px;top:3134px">
    <svg width="36" height="22" viewBox="0 0 36 22" fill="var(--purple)"><path d="M0 22V12C0 5 4 1 10 0v5c-3 1-4 3-4 6h5v11zM19 22V12c0-7 4-11 10-12v5c-3 1-4 3-4 6h5v11z"/></svg>
    <p>Lorem Ipsum is simply dummy text of the printing and typesetting industry. Lorem Ipsum has been the industry's standard dummy text ever</p>
    <div class="who"><b>MARA LIND</b><span>Manager</span></div>
  </div>
</section>

<div class="abs rule" style="top:3434px"></div>

<!-- news -->
<section class="news">
  <h2>LATEST NEWS &amp; BLOGS</h2>
  <div class="abs arrow prev" style="left:974px;top:3531px"><svg width="12" height="12" viewBox="0 0 12 12"><path d="M8 1L3 6l5 5" stroke="var(--purple)" stroke-width="2.4" fill="none"/></svg></div>
  <div class="abs arrow next" style="left:1026px;top:3531px"><svg width="12" height="12" viewBox="0 0 12 12"><path d="M4 1l5 5-5 5" stroke="#fff" stroke-width="2.4" fill="none"/></svg></div>

  <article class="abs post featured" style="left:135px;top:3620px">
    <div class="thumb" role="img" aria-label="Senior doctor checking on a patient in a hospital bed" style="background:linear-gradient(135deg,#d8d2c8,#bfb7aa 50%,#8f8a82)"></div>
    <h3>Lorem Ipsum is simply dummy...</h3>
    <div class="date">APRIL 08, 2022</div>
    <p>Lorem Ipsum is simply dummy text of the printing and typesetting industry.</p>
    <div class="more">READ MORE <svg width="8" height="10" viewBox="0 0 8 10"><path d="M2 1l4 4-4 4" stroke="var(--blue-dark)" stroke-width="1.8" fill="none"/></svg></div>
  </article>
  <article class="abs post" style="left:453px;top:3620px">
    <div class="thumb" role="img" aria-label="Medical staff in blue scrubs attending a patient" style="background:linear-gradient(135deg,#4b8fd0,#9ab8d6 50%,#5a6f8a)"></div>
    <h3>Lorem Ipsum is simply dummy...</h3>
    <div class="date">APRIL 08, 2022</div>
    <p>Lorem Ipsum is simply dummy text of the printing and typesetting industry.</p>
    <div class="more">READ MORE <svg width="8" height="10" viewBox="0 0 8 10"><path d="M2 1l4 4-4 4" stroke="var(--blue-dark)" stroke-width="1.8" fill="none"/></svg></div>
  </article>
  <article class="abs post" style="left:769px;top:3620px">
    <div class="thumb" role="img" aria-label="Doctor and nurse beside a patient in a warmly lit ward" style="background:linear-gradient(135deg,#e7823f,#e9a06b 45%,#c8ccd2)"></div>
    <h3>Lorem Ipsum is simply dummy...</h3>
    <div class="date">APRIL 08, 2022</div>
    <p>Lorem Ipsum is simply dummy text of the printing and typesetting industry.</p>
    <div class="more">READ MORE <svg width="8" height="10" viewBox="0 0 8 10"><path d="M2 1l4 4-4 4" stroke="var(--blue-dark)" stroke-width="1.8" fill="none"/></svg></div>
  </article>
</section>

<!-- partners -->
<div class="abs partner lifted" style="left:135px" aria-label="Partner badge"><i></i></div>
<div class="abs partner" style="left:373px" aria-label="Partner badge"><i></i></div>
<div class="abs partner" style="left:611px" aria-label="Partner badge"><i></i></div>
<div class="abs partner" style="left:850px" aria-label="Partner badge"><i></i></div>

<div class="abs rule" style="top:4319px"></div>

<!-- footer -->
<footer class="footer">
  <div class="brand"><span class="mark"></span>LOREM IPSUM</div>
  <p class="about-text">Lorem Ipsum is simply dummy text of the printing and typesetting industry. Lorem Ipsum has been the industry's standard dummy text ever since the 1500s.Lorem Ipsum is simply dummy text of the printing and typesetting industry.</p>
  <ul style="left:529px;top:4464px"><li>Investors</li><li>Careers</li><li>Media</li><li>Partners</li></ul>
  <ul style="left:706px;top:4464px"><li>Grant Seekers</li><li>Healthcare Professionals</li><li>Business to Business</li><li>Merchandise</li></ul>
  <ul style="left:965px;top:4464px"><li>Privacy Statement</li><li>Terms of Use</li><li>Contact Us</li></ul>
  <div class="abs copyright-rule"></div>
  <div class="abs copyright">© 2023 Clearwell Health Co. All rights reserved</div>
</footer>

</body>
</html>
```